Sole trader requires buisness card / company logo for mining and aviation

I require a business card and logo design having the following requirements;
Kestrel Airframe and Plant Services
Owner: Martin Hollis
Ph: 0491570156
E: martin-r-hollis@brolgamail.com.au

Logo should include a basic aircraft image and an image of an item of mining machinery either a dump truck or large excavator, but keeping in mind that the image is to be transferred onto clothing embroidery.

```html
<!DOCTYPE html>
<html lang="en">
<head>
<meta charset="utf-8">
<title>Kestrel Airframe and Plant Services – Business Card</title>
<link rel="stylesheet" href="https://fonts.googleapis.com/css2?family=Open+Sans:wght@400;700&display=swap">
<style>
  :root {
    --backdrop: #3d0d10;
    --card-white: #ffffff;
    --rule-grey: #b8b8b8;
    --brand-orange: #f07a22;
    --name-orange: #d9741f;
    --panel-dark: #26282a;
    --panel-dark-edge: #1b1c1e;
    --text-light: #f4f4f4;
  }
  * { margin: 0; padding: 0; box-sizing: border-box; }
  html, body {
    width: 1200px;
    height: 800px;
    overflow: hidden;
    background: var(--backdrop);
    font-family: "Open Sans", Arial, sans-serif;
  }
  .canvas {
    position: relative;
    width: 1200px;
    height: 800px;
  }
  .business-card {
    position: absolute;
    left: 150px;
    top: 143px;
    width: 900px;
    height: 514px;
    background: var(--card-white);
    overflow: hidden;
    box-shadow: 0 18px 40px rgba(0, 0, 0, 0.55);
  }
  .brand-area {
    position: absolute;
    left: 0;
    top: 0;
    width: 100%;
    height: 270px;
    display: flex;
    align-items: center;
    justify-content: center;
    gap: 16px;
  }
  .brand-mark {
    width: 22px;
    height: 22px;
    background: var(--brand-orange);
  }
  .brand-name {
    font-weight: 700;
    font-size: 38px;
    color: var(--brand-orange);
    letter-spacing: 0.5px;
  }
  .divider-grey {
    position: absolute;
    left: 0;
    top: 270px;
    width: 100%;
    height: 5px;
    background: var(--rule-grey);
  }
  .divider-orange {
    position: absolute;
    left: 0;
    top: 275px;
    width: 100%;
    height: 11px;
    background: var(--brand-orange);
  }
  .contact-panel {
    position: absolute;
    left: 0;
    top: 286px;
    width: 100%;
    height: 228px;
    background: linear-gradient(180deg, var(--panel-dark) 0%, var(--panel-dark-edge) 100%);
  }
  .contact-details {
    position: absolute;
    left: 0;
    top: 24px;
    width: 100%;
    padding-left: 120px;
    text-align: center;
    color: var(--text-light);
  }
  .person-name {
    font-weight: 700;
    font-size: 30px;
    line-height: 1.15;
    color: var(--name-orange);
  }
  .person-role {
    font-size: 15px;
    line-height: 1.3;
  }
  .phone {
    font-size: 29px;
    line-height: 1.3;
    margin-top: 22px;
  }
  .email {
    font-size: 29px;
    line-height: 1.3;
  }
</style>
</head>
<body>
  <main class="canvas">
    <section class="business-card" aria-label="Business card">
      <header class="brand-area">
        <span class="brand-mark" aria-hidden="true"></span>
        <span class="brand-name">Kestrel Airframe and Plant Services</span>
      </header>
      <div class="divider-grey"></div>
      <div class="divider-orange"></div>
      <div class="contact-panel">
        <div class="contact-details">
          <p class="person-name">Martin Hollis</p>
          <p class="person-role">Owner</p>
          <p class="phone">0491570156</p>
          <p class="email">martin-r-hollis@brolgamail.com.au</p>
        </div>
      </div>
    </section>
  </main>
</body>
</html>
```